CoinLantern one-page corporate website

Our company, CoinLantern is a cryptocurrency Initial Coin Offering ("ICO" marketing and promotion agency, which requires a professional company landing page design whereby prospective clients can learn;
-who we are
-what we do
-what our people are saying about us
-core team members
-subscribe to our mailing list
-how to get in touch (basic contact form)

We are looking for something unique and attractive -- not a standard Pako template that we could put together ourselves. Plain stock images should not be used. Unique visualizations of the service offerings and creative presentation are key. We are a cutting edge marketing agency and as such, we need to look the part.

Relevant documentation about the business and branding assets have been attached to guide the designer. Certain information will be included by the company at a later date such as team member descriptions. As such, lorem ipsum may be included wherever necessary to help visualize the textual areas.

****Please ensure that you actually utilize the photos and graphics provided so that we can have a good picture of what it would actually look like with our branding.

The site must be responsive HTML CSS Design.

Sites style themes we like for inspiration and specific sections we like ****Very important***:
https://vaultorbitra.example/offers - we like that the token & company logo is used in unique visualizations that connects various ideas together. We imagine unique visuals such as these with our Icon (see attached) serving as a token. We also like the unique and attractive visual theme of the webpage itself.

https://quarrelstone.example/ - we like the layout of this website, specifically how the service offerings are displayed in a circular visual graphic with the Quarrel logo in the middle. We imagine a similar type of graphic designed with CoinLantern in the middle.

https://zorvinet.example/ - we like how the logo is central to the theme in this site when you first enter and how it fades + shrinks into the distance as you scroll down.

Target Market(s)

cryptocurrency entrepreneurs and ICOs

Industry/Entity Type

It Company

Coding

Coded - Design and coding required

Number of Pages Required

1 page

Font styles to use
Sans Serif

Colors

Designer to choose colors to be used in the design.

Requirements
Must have
• The site must be responsive HTML CSS Design.
• The page must be modern and visually attractive. Elements must not be static and should have a fluid motion / visual change as the user scrolls through the page.
Should not have
• The project should not use any old stock images or elements which are dull and over-used, but rather images or elements should be unique and well thought out.

```html
<!DOCTYPE html>
<html lang="en">
<head>
<meta charset="utf-8">
<title>CoinLantern — Digital Token Capital Markets</title>
<link href="https://fonts.googleapis.com/css2?family=Montserrat:wght@400;600;700&family=Open+Sans:wght@400;600&display=swap" rel="stylesheet">
<style>
:root{
  --navy:#1d3f6b;
  --navy-deep:#15305a;
  --blue:#2a5b92;
  --sky:#2aa7e0;
  --ink:#2a2a2a;
  --muted:#7a7f86;
  --grey-bg:#ececec;
  --line:#d6d9dd;
  --footer:#1f2329;
  --footer-deep:#16191e;
  --white:#ffffff;
}
*{box-sizing:border-box;margin:0;padding:0}
html,body{width:1200px;height:3420px;overflow:hidden}
body{font-family:"Open Sans",Arial,sans-serif;color:var(--ink);background:var(--white);position:relative}
h2,h3,.heading{font-family:"Montserrat",Arial,sans-serif}
section,header,footer{position:absolute;left:0;width:1200px}

/* Hero */
.hero{top:0;height:652px;overflow:hidden}
.hero-photo{position:absolute;inset:0;background:linear-gradient(180deg,#27548a 0%,#3a6ea6 45%,#1d3f6b 100%)}
.hero-shade{position:absolute;inset:0;background:linear-gradient(90deg,rgba(21,48,90,.55),rgba(21,48,90,.15) 50%,rgba(21,48,90,.55))}
.nav{position:absolute;top:0;left:0;right:0;height:64px;display:flex;align-items:center;justify-content:space-between;padding:0 120px}
.brand{display:flex;align-items:center;gap:10px;color:var(--white);font-family:"Montserrat",sans-serif;font-weight:700;font-size:26px}
.brand-dot{width:30px;height:30px;border-radius:50%;background:var(--white)}
.brand-tag{display:block;font-size:9px;font-weight:400;letter-spacing:1px;margin-top:-2px}
.nav-links{display:flex;gap:26px;list-style:none;color:var(--white);font-family:"Montserrat",sans-serif;font-size:12px;font-weight:600}
.hero-title{position:absolute;top:296px;width:100%;text-align:center;color:var(--white);font-family:"Montserrat",sans-serif}
.hero-title .l1{font-size:34px;font-weight:400;letter-spacing:.5px}
.hero-title .l2{font-size:34px;font-weight:700;margin-top:10px}
.btn{display:inline-block;border:1px solid var(--white);border-radius:20px;color:var(--white);font-family:"Montserrat",sans-serif;font-size:11px;font-weight:600;padding:9px 28px;letter-spacing:.5px}
.hero .btn{position:absolute;top:512px;left:50%;transform:translateX(-50%);background:rgba(255,255,255,.08)}
.dots{position:absolute;top:606px;left:50%;transform:translateX(-50%);display:flex;gap:8px}
.dots span{width:10px;height:10px;border-radius:50%;border:1px solid var(--white)}
.dots span.on{background:var(--white)}

/* Section heads */
.sec-title{text-align:center;font-family:"Montserrat",sans-serif;font-weight:700;font-size:34px;color:var(--navy-deep)}
.sec-sub{text-align:center;font-size:11px;color:var(--muted);margin-top:6px}

.who{top:652px;height:236px;padding-top:58px}
.who p{width:780px;margin:22px auto 0;text-align:center;font-size:12px;line-height:20px;color:var(--muted)}

/* Services */
.what{top:888px;height:832px;background:var(--grey-bg);padding-top:30px}
.svc{position:absolute;display:flex;align-items:center;gap:16px;font-size:13px;color:#3c4048;line-height:18px}
.svc.left{flex-direction:row-reverse;text-align:right}
.svc-icon{width:58px;height:58px;border-radius:50%;background:var(--navy);flex:none;display:flex;align-items:center;justify-content:center;box-shadow:0 0 0 6px rgba(29,63,107,.12)}
.svc-text{width:200px}
.hub{position:absolute;left:480px;top:310px;width:240px;height:86px;display:flex;align-items:center;justify-content:center;gap:10px;font-family:"Montserrat",sans-serif;font-weight:700;font-size:28px;color:var(--navy)}
.hub-dot{width:40px;height:40px;border-radius:50%;background:var(--sky)}
.what .btn{position:absolute;top:660px;left:50%;transform:translateX(-50%);border-color:var(--navy);color:var(--navy)}

/* Testimonial */
.words{top:1720px;height:248px;background:var(--navy);color:var(--white);padding-top:34px}
.words .sec-title,.words .sec-sub{color:var(--white)}
.words .sec-sub{color:#c6d3e4}
.quote{position:absolute;left:132px;top:116px;width:940px;display:flex;gap:40px}
.quote-photo{width:136px;height:104px;background:linear-gradient(135deg,#8b8f95,#3e4248);flex:none}
.quote-mark{font-family:"Montserrat",sans-serif;font-size:48px;line-height:40px;font-weight:700}
.quote-body{font-size:12px;line-height:19px;color:#e6edf6}
.quote-name{font-size:12px;margin-top:8px;font-weight:600}

/* Team */
.team{top:1968px;height:480px;padding-top:56px}
.team-row{position:absolute;top:132px;left:128px;display:flex;gap:40px}
.card{width:208px;background:var(--white);box-shadow:0 4px 14px rgba(0,0,0,.18);text-align:center;padding-bottom:18px}
.card-photo{height:200px;background:linear-gradient(180deg,#b9bcc1,#4a4e55)}
.card h3{font-size:17px;margin-top:18px;color:var(--ink)}
.card p{font-size:10px;color:var(--muted);margin-top:4px}
.arrow{position:absolute;top:312px;width:24px;height:30px;border:1px solid #999;display:flex;align-items:center;justify-content:center}

/* Newsletter */
.news{top:2448px;height:192px;background:var(--navy);color:var(--white);text-align:center;padding-top:42px}
.news .sec-title{color:var(--white);font-size:30px}
.news .sec-sub{color:#c6d3e4}
.sub-form{display:flex;justify-content:center;margin-top:22px}
.sub-input{width:220px;height:34px;background:var(--white);color:#9aa0a8;font-size:11px;text-align:left;padding:10px 12px}
.sub-btn{width:100px;height:34px;background:var(--sky);font-family:"Montserrat",sans-serif;font-size:11px;font-weight:600;padding-top:10px}

/* Contact */
.contact{top:2640px;height:460px;padding-top:40px}
.form{position:absolute;left:280px;top:140px;width:660px;display:grid;grid-template-columns:1fr 1fr;gap:24px 20px}
.field{height:40px;border:1px solid var(--line);display:flex;align-items:center;gap:10px;padding:0 12px;font-size:11px;color:#9aa0a8}
.field.msg{grid-column:1 / span 2;height:80px;align-items:flex-start;padding-top:12px}
.contact .btn{position:absolute;top:384px;left:50%;transform:translateX(-50%);border-color:var(--navy);color:var(--navy)}

/* Footer */
.footer{top:3100px;height:320px;background:var(--footer);color:#c7ccd3}
.foot-band{position:absolute;left:120px;top:12px;width:960px;height:68px;background:var(--navy);display:flex;align-items:center;justify-content:space-between;padding:0 28px;font-size:11px;color:var(--white)}
.socials{display:flex;gap:10px}
.socials span{width:24px;height:24px;border-radius:50%;border:1px solid var(--white)}
.band-item{display:flex;align-items:center;gap:10px;line-height:16px}
.foot-body{position:absolute;left:120px;top:104px;width:960px;display:flex;gap:48px;font-size:11px;line-height:18px}
.foot-brand{width:220px}
.foot-brand .brand{font-size:22px}
.foot-brand p{margin-top:12px;color:#9097a0}
.foot-col h4{font-family:"Montserrat",sans-serif;color:var(--white);font-size:15px;margin-bottom:10px}
.foot-col ul{list-style:none;font-size:10px;color:#9097a0}
.hours{margin-left:auto;width:220px;font-size:11px;color:var(--white);line-height:30px}
.hours .closed{color:var(--sky)}
.top-btn{position:absolute;right:120px;top:260px;width:24px;height:24px;background:var(--navy)}
.copy{position:absolute;bottom:0;left:0;right:0;height:28px;background:var(--footer-deep);text-align:center;font-size:10px;color:#9097a0;padding-top:7px}
</style>
</head>
<body>

<header class="hero">
  <div class="hero-photo" role="img" aria-label="Blue-toned city skyline photograph behind the headline"></div>
  <div class="hero-shade"></div>
  <nav class="nav">
    <div class="brand"><span class="brand-dot"></span><span>CoinLantern<span class="brand-tag">The Token Sale Experts</span></span></div>
    <ul class="nav-links"><li>HOME</li><li>ABOUT</li><li>TESTIMONIALS</li><li>TEAM</li><li>CONTACT</li></ul>
  </nav>
  <div class="hero-title">
    <div class="l1">A FULL-SERVICE INVESTMENT BANK FOR</div>
    <div class="l2">THE DIGITAL TOKEN CAPITAL MARKETS</div>
  </div>
  <span class="btn">KNOW MORE ›</span>
  <div class="dots"><span></span><span class="on"></span><span></span></div>
</header>

<section class="who">
  <h2 class="sec-title">WHO WE ARE</h2>
  <p>Lorem ipsum dolor sit amet, consectetur adipiscing elit. Nam vel nunc nec est finibus hendrerit id et nunc. Curabitur ut ligula sed ex fermentum tempus. Etiam tincidunt, orci vitae faucibus tristique, lectus arcu ornare massa, ut tempor enim tellus ac velit. Cras eget eros sem, id tincidunt diam.</p>
</section>

<section class="what">
  <h2 class="sec-title">WHAT WE DO</h2>
  <div class="sec-sub">We run every token sale from idea to listing</div>

  <svg width="1200" height="832" style="position:absolute;left:0;top:0" aria-hidden="true">
    <g stroke="#b7c2d0" stroke-width="1" stroke-dasharray="4 4" fill="none">
      <line x1="600" y1="352" x2="500" y2="160"/><line x1="600" y1="352" x2="700" y2="160"/>
      <line x1="600" y1="352" x2="410" y2="272"/><line x1="600" y1="352" x2="790" y2="272"/>
      <line x1="600" y1="352" x2="410" y2="412"/><line x1="600" y1="352" x2="790" y2="412"/>
      <line x1="600" y1="352" x2="500" y2="524"/><line x1="600" y1="352" x2="700" y2="524"/>
    </g>
  </svg>

  <div class="svc left" style="left:242px;top:131px"><span class="svc-icon"><svg width="24" height="24" viewBox="0 0 24 24" fill="none" stroke="#fff" stroke-width="2"><rect x="4" y="10" width="4" height="10"/><rect x="10" y="6" width="4" height="14"/><rect x="16" y="3" width="4" height="17"/></svg></span><span class="svc-text">Corporate Finance</span></div>
  <div class="svc" style="left:671px;top:131px"><span class="svc-icon"><svg width="24" height="24" viewBox="0 0 24 24" fill="none" stroke="#fff" stroke-width="2"><circle cx="12" cy="12" r="8"/><path d="M12 4v8h8"/></svg></span><span class="svc-text">Asset Management<br>&amp; Investments</span></div>
  <div class="svc left" style="left:152px;top:243px"><span class="svc-icon"><svg width="24" height="24" viewBox="0 0 24 24" fill="none" stroke="#fff" stroke-width="2"><path d="M4 18l6-6 4 4 6-8"/></svg></span><span class="svc-text">Strategic and M&amp;A<br>Advisory</span></div>
  <div class="svc" style="left:761px;top:243px"><span class="svc-icon"><svg width="24" height="24" viewBox="0 0 24 24" fill="none" stroke="#fff" stroke-width="2"><path d="M4 8h14l-3-3M20 16H6l3 3"/></svg></span><span class="svc-text">Trading, FX &amp;<br>Market Making</span></div>
  <div class="svc left" style="left:152px;top:383px"><span class="svc-icon"><svg width="24" height="24" viewBox="0 0 24 24" fill="none" stroke="#fff" stroke-width="2"><path d="M12 3v18M5 8h14M7 8l-3 7h6zM17 8l-3 7h6z"/></svg></span><span class="svc-text">Tax &amp; Legal Structuring</span></div>
  <div class="svc" style="left:761px;top:383px"><span class="svc-icon"><svg width="24" height="24" viewBox="0 0 24 24" fill="none" stroke="#fff" stroke-width="2"><rect x="4" y="10" width="16" height="10"/><path d="M8 10V7a4 4 0 0 1 8 0v3"/></svg></span><span class="svc-text">Settlement, Depository<br>&amp; Custody Services</span></div>
  <div class="svc left" style="left:242px;top:495px"><span class="svc-icon"><svg width="24" height="24" viewBox="0 0 24 24" fill="none" stroke="#fff" stroke-width="2"><circle cx="12" cy="12" r="8"/><path d="M12 7v10M9 10h5a2 2 0 0 1 0 4H9"/></svg></span><span class="svc-text">Issuance and Underwriting<br>(ICO/Token Sales)</span></div>
  <div class="svc" style="left:671px;top:495px"><span class="svc-icon"><svg width="24" height="24" viewBox="0 0 24 24" fill="none" stroke="#fff" stroke-width="2"><rect x="4" y="5" width="16" height="11"/><path d="M9 20h6M12 16v4"/></svg></span><span class="svc-text">Technical and Platform Solutions<br>(Smart Contracts, AML, KYC)</span></div>

  <div class="hub"><span class="hub-dot"></span>CoinLantern</div>
  <span class="btn">CORE TEAM MEMBERS ›</span>
</section>

<section class="words">
  <h2 class="sec-title">CLIENT'S WORDS</h2>
  <div class="sec-sub">What our people are saying about us</div>
  <div class="quote">
    <div class="quote-photo" role="img" aria-label="Portrait photo of the client"></div>
    <div class="quote-mark">“</div>
    <div>
      <p class="quote-body">Lorem ipsum dolor sit amet, consectetur adipiscing elit. Nam vel nunc nec est finibus hendrerit id et nunc. Curabitur ut ligula sed ex fermentum tempus. Etiam tincidunt, orci vitae faucibus tristique, lectus arcu ornare massa, ut tempor enim tellus ac velit.</p>
      <p class="quote-name">- Lena Farrow</p>
    </div>
  </div>
</section>

<section class="team">
  <h2 class="sec-title">CORE TEAM MEMBERS</h2>
  <div class="sec-sub">Dedicated, professional and passionate about tokens</div>
  <span class="arrow" style="left:96px"><svg width="10" height="14" viewBox="0 0 10 14"><path d="M8 1L2 7l6 6" stroke="#777" stroke-width="2" fill="none"/></svg></span>
  <div class="team-row">
    <div class="card"><div class="card-photo" role="img" aria-label="Black and white portrait of team member"></div><h3>MIRA HOLT</h3><p>CEO &amp; Founder</p></div>
    <div class="card"><div class="card-photo" role="img" aria-label="Black and white portrait of team member"></div><h3>OREN VALE</h3><p>Lead Designer &amp; Founder</p></div>
    <div class="card"><div class="card-photo" role="img" aria-label="Black and white portrait of team member"></div><h3>TESSA ROWE</h3><p>PR &amp; Marketing</p></div>
    <div class="card"><div class="card-photo" role="img" aria-label="Black and white portrait of team member"></div><h3>IDRIS CRANE</h3><p>Senior Developer</p></div>
  </div>
  <span class="arrow" style="left:1080px"><svg width="10" height="14" viewBox="0 0 10 14"><path d="M2 1l6 6-6 6" stroke="#777" stroke-width="2" fill="none"/></svg></span>
</section>

<section class="news">
  <h2 class="sec-title">JOIN OUR NEWSLETTER</h2>
  <div class="sec-sub">Sign up for our newsletter</div>
  <div class="sub-form"><div class="sub-input">Enter your email address</div><div class="sub-btn">SUBSCRIBE</div></div>
</section>

<section class="contact">
  <h2 class="sec-title">KEEP IN TOUCH</h2>
  <div class="sec-sub">Send us a note and we will reply within one day</div>
  <div class="form">
    <div class="field"><svg width="12" height="12" viewBox="0 0 12 12" fill="#aaa"><circle cx="6" cy="4" r="3"/><path d="M0 12a6 5 0 0 1 12 0z"/></svg>Name</div>
    <div class="field"><svg width="12" height="12" viewBox="0 0 12 12" fill="none" stroke="#aaa" stroke-width="1.5"><path d="M2 1h3l1 3-2 1a7 7 0 0 0 3 3l1-2 3 1v3c-6 0-10-4-10-9z"/></svg>Phone</div>
    <div class="field"><svg width="12" height="10" viewBox="0 0 12 10" fill="none" stroke="#aaa"><rect x=".5" y=".5" width="11" height="9"/><path d="M.5 .5l5.5 5 5.5-5"/></svg>Email</div>
    <div class="field"><svg width="12" height="12" viewBox="0 0 12 12" fill="none" stroke="#aaa"><path d="M1 3h10M1 6h10M1 9h6"/></svg>Subject</div>
    <div class="field msg"><svg width="12" height="12" viewBox="0 0 12 12" fill="none" stroke="#aaa"><path d="M1 11l2-4 6-6 2 2-6 6z"/></svg>Message</div>
  </div>
  <span class="btn">SEND MESSAGE ›</span>
</section>

<footer class="footer">
  <div class="foot-band">
    <div class="socials"><span></span><span></span><span></span><span></span></div>
    <div class="band-item"><svg width="14" height="18" viewBox="0 0 14 18" fill="#fff"><path d="M7 0a7 7 0 0 1 7 7c0 5-7 11-7 11S0 12 0 7a7 7 0 0 1 7-7zm0 4a3 3 0 1 0 0 6 3 3 0 0 0 0-6z"/></svg><span>4120 Harbor Lane South,<br>Westfield, NY 10400</span></div>
    <div class="band-item"><svg width="16" height="16" viewBox="0 0 12 12" fill="#fff"><path d="M2 1h3l1 3-2 1a7 7 0 0 0 3 3l1-2 3 1v3c-6 0-10-4-10-9z"/></svg><span>(555) 010-2144<br>(555) 010-2145</span></div>
    <div class="band-item"><svg width="16" height="12" viewBox="0 0 12 10" fill="none" stroke="#fff"><rect x=".5" y=".5" width="11" height="9"/><path d="M.5 .5l5.5 5 5.5-5"/></svg><span>hello@coinlantern.example<br>info@coinlantern.example</span></div>
  </div>
  <div class="foot-body">
    <div class="foot-brand">
      <div class="brand"><span class="brand-dot"></span><span>CoinLantern<span class="brand-tag">The Token Sale Experts</span></span></div>
      <p>Lorem ipsum dolor sit amet, consectetur adipiscing elit. Vestibulum nec nisl vel arcu viverra dictum at.</p>
    </div>
    <div class="foot-col"><h4>USEFUL LINKS</h4><ul><li>PRIVATE INVESTMENTS</li><li>TOKEN SALE CONSULTING</li><li>PRIVACY</li><li>WHITE PAPER REVIEW</li><li>FAQ</li></ul></div>
    <div class="foot-col"><h4>USEFUL LINKS</h4><ul><li>MARKETING</li><li>PARTNERSHIP</li><li>CAREERS</li><li>SUPPORT</li><li>BLOG</li></ul></div>
    <div class="hours">Mon - Friday : 9:00am - 06:00pm<br>Saturday 10:00am - 02:00pm<br><span class="closed">Sunday : CLOSED</span></div>
  </div>
  <span class="top-btn"><svg width="24" height="24" viewBox="0 0 24 24"><path d="M7 14l5-5 5 5" stroke="#fff" stroke-width="2" fill="none"/></svg></span>
  <div class="copy">CoinLantern © Copyright 2017</div>
</footer>

</body>
</html>
```